Complete Re-Design of brentholloway.com

We are looking for a designer/developer that can create a personal branding website design for BrentHolloway.com. The current site is live and operational, but needs a complete redesign to make it more modern, professional, stunning, and to really showcase Brent and his expertise.
We need all the same content and services currently on the site to be migrated over, so keep that in mind when designing the homepage. We want layout, colors, style, and features that will really impress visitors and keep them engaged on the website and ultimately to purchase our services. Ultimately our goal is to gain clients and customers, and to make brent stand out as a trusted expert in his field.
Brent is a domain expert, public speaker, mentor, and coach, a serial entrepreneur and owner of multiple successful online businesses. Please read and review BrentHolloway.com to get a good idea of his background, personality, and what he offers.
An example of a personal branding site that we are impressed with is www.mikefenwright.com, however we do NOT necessarily want to copy his site, just use it as a reference for the level of quality we are looking for. We want lots of ideas and options, you as the designer may have unique and innovative ideas that we havent thought of yet that will blow us away. We want to see your creativity in action.
Number of Pages Required
1 page
Requirements
Must have
- https://www.filevaultz.com/sh/qk372pzrtwnb18xd/KLMtrQWpZnVcRsDxGhJYkLmNa?oref=e
- file vaultz link to photos of Brent you can use.
- Must include the current features and options on our current navigation menu, but they can be featured and showcased in a different better way
- This is for an public figure/expert/entreprenuer who is looking to take his personal brand to the next level, and also redesign his website to reflect that.
- We already have a lot of content and images, and videos from his previous site that would need to be transferred over.
Should not have
- Old outdated colors, fonts, images, style. Nothing too feminine.

```html
<!DOCTYPE html>
<html lang="en">
<head>
<meta charset="utf-8">
<title>Brent Holloway – Domain Expert</title>
<link href="https://fonts.googleapis.com/css2?family=PT+Sans:ital,wght@0,400;0,700;1,400;1,700&family=Open+Sans:ital,wght@0,400;0,600;0,700;1,400&display=swap" rel="stylesheet">
<style>
:root{
  --navy:#1c2a5c;
  --navy-deep:#15214a;
  --navy-mid:#243768;
  --teal:#3f9aab;
  --teal-soft:#5fb2c0;
  --ink:#2a2a2a;
  --muted:#555b66;
  --paper:#f4f4f4;
  --white:#ffffff;
}
*{margin:0;padding:0;box-sizing:border-box}
html,body{width:1200px;height:3509px;overflow:hidden}
body{font-family:"Open Sans",Arial,sans-serif;color:var(--ink);background:var(--white);position:relative}
.abs{position:absolute}

/* header */
.site-header{position:absolute;left:0;top:0;width:1200px;height:112px;background:var(--white)}
.brand{position:absolute;left:96px;top:36px;font-family:"PT Sans",sans-serif;font-weight:700;font-size:30px;color:var(--navy);letter-spacing:-.3px}
.main-nav{position:absolute;left:460px;top:48px;display:flex;gap:33px;font-size:13px;color:#555;letter-spacing:.2px}
.main-nav .active{color:var(--navy);font-weight:600}

/* hero */
.hero{position:absolute;left:0;top:112px;width:1200px;height:562px;background:linear-gradient(90deg,#e3e5ea,#f3f4f6 45%,#eceef2)}
.hero-portrait{position:absolute;left:95px;top:28px;width:365px;height:534px;background:linear-gradient(180deg,#c9ccd3 0%,#3c4660 45%,#222a40 100%);border-radius:4px 4px 0 0}
.hero-title{position:absolute;left:530px;top:40px;font-family:"PT Sans",sans-serif;font-weight:700;font-size:58px;line-height:64px;color:var(--navy)}
.hero-sub{position:absolute;left:533px;top:180px;font-size:14px;font-weight:600;color:#333;letter-spacing:.3px}
.checklist{position:absolute;top:250px;list-style:none;font-size:14px;color:#333}
.checklist li{height:29px;display:flex;align-items:center;gap:10px}
.checklist svg{width:13px;height:13px}
.optin{position:absolute;left:535px;top:373px;width:563px;height:80px;background:#a7adbd;display:flex;align-items:center;gap:8px;padding:0 14px}
.optin .field{height:42px;background:var(--white);font-size:13px;color:#555;display:flex;align-items:center;padding-left:14px}
.optin .f1{width:183px}.optin .f2{width:183px}
.optin .cta{height:42px;width:158px;background:var(--teal-soft);color:var(--white);font-size:12px;font-weight:700;display:flex;align-items:center;justify-content:center}
.privacy{position:absolute;left:535px;top:478px;font-size:12px;font-weight:700;color:var(--navy)}

/* about */
.about{position:absolute;left:0;top:674px;width:1200px;height:467px;background:var(--paper);text-align:center}
.section-title{font-family:"PT Sans",sans-serif;font-size:32px;font-weight:400;color:#222}
.about .section-title{position:absolute;left:0;width:1200px;top:40px}
.about-intro{position:absolute;left:225px;width:750px;top:90px;font-size:12px;line-height:20px;color:#333}
.service{position:absolute;top:162px;width:270px}
.service .icon{width:128px;height:128px;border-radius:50%;background:var(--teal);margin:0 auto;display:flex;align-items:center;justify-content:center}
.service h3{font-weight:400;font-size:17px;margin-top:32px;color:#222}
.service p{font-size:11.5px;line-height:19px;color:#444;margin-top:14px}

/* awards */
.awards{position:absolute;left:0;top:1141px;width:1200px;height:445px;background:#f2f2f2}
.awards-panel{position:absolute;left:0;top:0;width:498px;height:445px;background:linear-gradient(120deg,#3a4f7e,#1f2f5e 60%,#1a2853)}
.awards-panel h2{position:absolute;right:58px;top:115px;text-align:right;font-family:"PT Sans",sans-serif;font-weight:700;font-size:33px;line-height:42px;color:var(--white);letter-spacing:.5px}
.awards-panel p{position:absolute;right:58px;top:226px;font-size:14px;color:#dfe3ee}
.btn-outline{position:absolute;border:1px solid rgba(255,255,255,.85);color:var(--white);font-size:12px;display:flex;align-items:center;justify-content:center;letter-spacing:.3px}
.awards-note{position:absolute;left:533px;top:42px;width:580px;font-size:12px;line-height:21px;color:#222}
.award-tile{position:absolute;top:142px;width:227px;height:258px;border-radius:8px}

/* book */
.book{position:absolute;left:0;top:1586px;width:1200px;height:484px;background:var(--paper)}
.book h2{position:absolute;left:98px;top:118px;font-family:"PT Sans",sans-serif;font-size:40px;font-weight:400;color:#222}
.book p{position:absolute;left:98px;top:182px;width:545px;font-size:11.5px;line-height:21px;color:#333}
.btn-teal{position:absolute;background:var(--teal);color:var(--white);font-size:12px;display:flex;align-items:center;justify-content:center;letter-spacing:.3px}
.book-cover{position:absolute;left:735px;top:68px;width:355px;height:356px;background:linear-gradient(135deg,#d8dadd,#bfc3c8 50%,#9a8a6a);border-radius:3px}

/* speaking */
.speaking{position:absolute;left:0;top:2070px;width:1200px;height:444px;background:linear-gradient(90deg,#1d2b5a,#243664 55%,#2a3d6c)}
.speaking h2{position:absolute;left:98px;top:78px;font-family:"PT Sans",sans-serif;font-weight:700;font-size:60px;color:var(--white)}
.speaking p{position:absolute;left:98px;top:178px;width:570px;font-style:italic;font-size:17px;line-height:29px;color:#e6e9f2}
.play{position:absolute;left:782px;top:110px}
.play-label{position:absolute;left:740px;top:302px;width:260px;text-align:center;font-size:12px;font-weight:700;color:var(--white)}

/* blog */
.blog{position:absolute;left:0;top:2514px;width:1200px;height:562px;background:var(--white)}
.blog h2{position:absolute;left:98px;top:30px;font-family:"PT Sans",sans-serif;font-weight:700;font-size:40px;color:#222}
.blog-intro{position:absolute;left:98px;top:92px;width:700px;font-style:italic;font-size:14px;line-height:23px;color:var(--teal)}
.post{position:absolute;top:182px;width:310px}
.post .thumb{width:310px;height:190px}
.post h3{font-weight:400;font-size:18px;margin-top:18px;color:#222}
.post .date{font-size:11px;color:var(--teal);margin-top:14px}
.post p{font-size:11px;line-height:20px;color:#444;margin-top:12px}

/* footer */
.site-footer{position:absolute;left:0;top:3076px;width:1200px;height:351px;background:var(--navy)}
.footer-brand{position:absolute;left:98px;top:34px;font-family:"PT Sans",sans-serif;font-weight:700;font-size:24px;color:var(--white)}
.footer-contact{position:absolute;left:615px;top:36px;height:38px;display:flex;align-items:center;font-size:14px;color:var(--white)}
.footer-heading{position:absolute;top:118px;font-size:14px;color:var(--white);letter-spacing:.3px}
.footer-rule{position:absolute;top:148px;height:1px;background:rgba(255,255,255,.25)}
.link-col{position:absolute;top:162px;list-style:none;font-size:11.5px;color:#dfe3ee}
.link-col li{height:26px;line-height:26px}
.bottom-bar{position:absolute;left:0;top:3427px;width:1200px;height:82px;background:var(--navy-deep);font-size:11px;color:#cfd5e4}
.social{position:absolute;top:28px;width:26px;height:26px;border-radius:2px}
</style>
</head>
<body>

<header class="site-header">
  <div class="brand">Brent Holloway</div>
  <nav class="main-nav">
    <span class="active">HOME</span><span>ABOUT</span><span>BLOG</span><span>PRESS</span><span>SERVICES</span><span>RESOURCES</span><span>BOOK BRENT</span><span>CONTACT</span>
  </nav>
</header>

<section class="hero">
  <div class="hero-portrait" role="img" aria-label="Portrait of Brent Holloway in a dark suit and tie"></div>
  <h1 class="hero-title">Join My New Business<br>Bootcamp for Free!</h1>
  <div class="hero-sub">NEMO ENIM IPSAM VOLUPTATEM QUIA VOLUPTAS SIT ASPERNATUR</div>
  <ul class="checklist" style="left:535px">
    <li><svg viewBox="0 0 13 13"><path d="M1 7l4 4 7-9" fill="none" stroke="#222" stroke-width="2.2"/></svg>Cool Site Plugins</li>
    <li><svg viewBox="0 0 13 13"><path d="M1 7l4 4 7-9" fill="none" stroke="#222" stroke-width="2.2"/></svg>Domain Instructional Videos</li>
    <li><svg viewBox="0 0 13 13"><path d="M1 7l4 4 7-9" fill="none" stroke="#222" stroke-width="2.2"/></svg>Great Services for Domainers</li>
  </ul>
  <ul class="checklist" style="left:825px">
    <li><svg viewBox="0 0 13 13"><path d="M1 7l4 4 7-9" fill="none" stroke="#222" stroke-width="2.2"/></svg>Great Tools for Domainers</li>
    <li><svg viewBox="0 0 13 13"><path d="M1 7l4 4 7-9" fill="none" stroke="#222" stroke-width="2.2"/></svg>Domain Conferences</li>
    <li><svg viewBox="0 0 13 13"><path d="M1 7l4 4 7-9" fill="none" stroke="#222" stroke-width="2.2"/></svg>Domain Companies</li>
  </ul>
  <form class="optin">
    <div class="field f1">Name</div>
    <div class="field f2">E - Mail Address</div>
    <div class="cta">GET INSTANT ACCESS</div>
  </form>
  <div class="privacy">100% PRIVACY, GUARANTEED!</div>
</section>

<section class="about">
  <h2 class="section-title">ABOUT OUR COMPANY</h2>
  <p class="about-intro">Lorem ipsum dolor sit amet, consectetur adipiscing elit, sed do eiusmod tempor incididunt ut labore et dolore magna aliqua. Ut enim ad minim veniam, quis nostrud exercitation ullamco laboris nisi ut aliquip ex ea commodo consequat.</p>
  <div class="service" style="left:126px">
    <div class="icon"><svg width="64" height="64" viewBox="0 0 64 64"><circle cx="32" cy="32" r="26" fill="#fff"/><rect x="4" y="26" width="56" height="13" fill="var(--teal)"/><text x="32" y="37" text-anchor="middle" font-family="Open Sans,sans-serif" font-weight="700" font-size="11" fill="#fff">WWW</text></svg></div>
    <h3>Domain Expert</h3>
    <p>Lorem ipsum dolor sit amet, consectetur adipisicing elit, sed do eiusmod tempor incididunt ut labore et dolore magna aliqua. eiusmod</p>
  </div>
  <div class="service" style="left:465px">
    <div class="icon"><svg width="64" height="50" viewBox="0 0 64 50"><rect x="10" y="4" width="44" height="30" rx="2" fill="none" stroke="#fff" stroke-width="4"/><path d="M2 40h60l-4 6H6z" fill="#fff"/></svg></div>
    <h3>SEO Specialist</h3>
    <p>Lorem ipsum dolor sit amet, consectetur adipisicing elit, sed do eiusmod tempor incididunt ut labore et dolore magna aliqua. eiusmod</p>
  </div>
  <div class="service" style="left:809px">
    <div class="icon"><svg width="60" height="50" viewBox="0 0 60 50"><path d="M4 17h10l14-12v40L14 33H4z" fill="#fff"/><path d="M36 16a12 12 0 010 18M42 10a20 20 0 010 30" fill="none" stroke="#fff" stroke-width="4" stroke-linecap="round"/></svg></div>
    <h3>Public Speaker</h3>
    <p>Lorem ipsum dolor sit amet, consectetur adipisicing elit, sed do eiusmod tempor incididunt ut labore et dolore magna aliqua. eiusmod</p>
  </div>
</section>

<section class="awards">
  <div class="awards-panel" role="img" aria-label="Faded photo of Brent Holloway on stage behind a navy overlay">
    <h2>DOMAIN<br>AWARDS</h2>
    <p>Companies owned by Brent Holloway</p>
    <div class="btn-outline" style="left:276px;top:270px;width:161px;height:48px">DOMAIN AWARDS</div>
  </div>
  <p class="awards-note">NameHub Forum / Brent Holloway was awarded the 2006, 2007, 2008, 2009, and 2010 'Domain Insight Award' as the best online community to discuss, buy, and sell domains. NameHub Forum was named best online forum by 'Registry Report' four out of the last five years.</p>
  <div class="award-tile" style="left:533px;background:radial-gradient(circle at 50% 42%,#b7793f 0 34%,#5a3a22 35%,#1d1f24 70%)" role="img" aria-label="Bronze developer of the year award medal"></div>
  <div class="award-tile" style="left:816px;background:linear-gradient(160deg,#cfc8c4,#7b6a66 45%,#3a3640)" role="img" aria-label="Brent Holloway receiving an award plaque with a colleague"></div>
</section>

<section class="book">
  <h2>THE BOOK</h2>
  <p>Lorem ipsum dolor sit amet, consectetur adipiscing elit, sed do eiusmod tempor incididunt ut labore et dolore magna aliqua. Ut enim ad minim veniam, quis nostrud exercitation ullamco laboris nisi ut aliquip ex ea commodo consequat. Duis aute irure dolor in reprehenderit in voluptate velit esse cillum dolore eu fugiat nulla pariatur. Excepteur sint occaecat cupidatat non proident, sunt in culpa qui officia deserunt mollit anim id est laborum</p>
  <div class="btn-teal" style="left:98px;top:317px;width:124px;height:37px">READ MORE</div>
  <div class="book-cover" role="img" aria-label="Two copies of Brent Holloway's book on investing in domain names"></div>
</section>

<section class="speaking" role="img" aria-label="Brent Holloway working at a computer, under a dark blue overlay">
  <h2>Speaking</h2>
  <p>Lorem ipsum dolor sit amet, consectetur adipiscing elit, sed do eius- mod tempor incididunt ut labore et dolore magna aliqua. Ut enim ad minim veniam, quis nostrud</p>
  <div class="btn-outline" style="left:100px;top:306px;width:162px;height:45px">LEARN MORE</div>
  <svg class="play" width="168" height="168" viewBox="0 0 168 168"><circle cx="84" cy="84" r="80" fill="none" stroke="rgba(255,255,255,.45)" stroke-width="3"/><path d="M68 56l42 28-42 28z" fill="none" stroke="rgba(255,255,255,.55)" stroke-width="3"/></svg>
  <div class="play-label">CLICK TO PLAY THE VIDEO</div>
</section>

<section class="blog">
  <h2>THE BLOG</h2>
  <p class="blog-intro">Lorem ipsum dolor sit amet, consectetur adipiscing elit, sed do eiusmod tempor incididunt ut labore et dolore magna aliqua. Ut enim ad minim veniam, quis nostrud</p>
  <div class="btn-teal" style="left:865px;top:62px;width:201px;height:46px">READ ALL BLOG POSTS</div>
  <article class="post" style="left:98px">
    <div class="thumb" role="img" aria-label="Brent Holloway at a desk with several monitors" style="background:linear-gradient(135deg,#8a9096,#3b4048 55%,#1e2228)"></div>
    <h3>Lorem ipsum dolor sit amet,</h3>
    <div class="date">02 - MARCH - 2015</div>
    <p>Lorem ipsum dolor sit amet, consectetur adipiscing elit. Sed blandit massa vel mauris sollicitudin dignissim. Lorem ipsum dolor sit amet, consectetur</p>
  </article>
  <article class="post" style="left:444px">
    <div class="thumb" role="img" aria-label="Portrait of Brent Holloway in a blue shirt" style="background:linear-gradient(135deg,#d9dadc,#a9b4c8 50%,#6b7a98)"></div>
    <h3>Lorem ipsum dolor sit amet,</h3>
    <div class="date">02 - MARCH - 2015</div>
    <p>Lorem ipsum dolor sit amet, consectetur adipiscing elit. Sed blandit massa vel mauris sollicitudin dignissim. Lorem ipsum dolor sit amet, consectetur</p>
  </article>
  <article class="post" style="left:789px">
    <div class="thumb" role="img" aria-label="Close portrait of Brent Holloway against a dark background" style="background:linear-gradient(135deg,#4a3c34,#7a6c64 45%,#2a2522)"></div>
    <h3>Lorem ipsum dolor sit amet,</h3>
    <div class="date">02 - MARCH - 2015</div>
    <p>Lorem ipsum dolor sit amet, consectetur adipiscing elit. Sed blandit massa vel mauris sollicitudin dignissim. Lorem ipsum dolor sit amet, consectetur</p>
  </article>
</section>

<footer class="site-footer">
  <div class="footer-brand">Brent Holloway</div>
  <div class="footer-contact">Call Us Today! (855) 410 - 7392 &nbsp;|&nbsp; support@brightlane.ca</div>
  <div class="btn-teal" style="left:979px;top:36px;width:121px;height:38px">CONTACT US</div>
  <div class="footer-heading" style="left:98px">CATEGORIES</div>
  <div class="footer-rule" style="left:98px;width:180px"></div>
  <ul class="link-col" style="left:98px"><li>Cool Site Plugins</li><li>NameHub Forum</li><li>Domain Companies</li><li>domain conferences</li><li>Domain Instructional Videos</li><li>Domain Sales</li></ul>
  <ul class="link-col" style="left:297px"><li>Domain Software</li><li>ecommerce</li><li>Searchly</li><li>Great Services for Domainers</li><li>Great Tools for Domainers</li><li>Introduction Video</li></ul>
  <ul class="link-col" style="left:484px"><li>Promo Codes</li><li>Recent Domain News</li><li>Sales Videos</li><li>Search Engines</li><li>Seo software</li><li>Software Reviews</li></ul>
  <div class="footer-heading" style="left:745px">WATCH BRENT'S VIDEOS</div>
  <div class="footer-rule" style="left:745px;width:355px"></div>
  <ul class="link-col" style="left:745px"><li>Differentiating Good Domain Names from the Crappy Ones</li><li>How to Sell a Domain Name</li><li>Online Reputation Repair: Seeing a New Business Opportunity</li><li>The 20 Most Influential People In The Domain Industry, 3 Years Later</li><li>THE ART OF THE NAME</li></ul>
</footer>

<div class="bottom-bar">
  <span class="abs" style="left:117px;top:34px">Connect with Us</span>
  <span class="social" style="left:222px;background:#d34836"></span>
  <span class="social" style="left:255px;background:#3b5a9a"></span>
  <span class="social" style="left:288px;background:#2a9fd6"></span>
  <span class="social" style="left:321px;background:#1f76b0"></span>
  <span class="social" style="left:354px;background:#c4302b"></span>
  <span class="abs" style="left:620px;top:34px">Copyright 2015 | All Rights Reserved | Powered by Sitecraftly.com | A Brightlane company</span>
</div>

</body>
</html>
```